EPS Environmental Profile Report

This report covers environmental considerations for EPS foam protective packaging. It is geared for high level international government officials so it must have a clean, professional look. We would like to have this document in an in-design file.

Please use the Unified EPS Trade Coalition (UETC) logo and colors for this document. We do not have a specific font, we've been using Calibri Light but welcome other suggestions to improve the overall document desgin.

```html
<!DOCTYPE html>
<html lang="en">
<head>
<meta charset="utf-8">
<title>EPS Environmental Profile Report</title>
<link rel="stylesheet" href="https://fonts.googleapis.com/css2?family=Barlow:ital,wght@0,400;0,700;1,400;1,600&family=Barlow+Semi+Condensed:wght@300&family=Oswald:wght@600&display=swap">
<style>
  :root{
    --navy:#1d3c5a;
    --orange:#f2ae30;
    --ink:#2e2e2e;
    --white:#ffffff;
    --photo-warm:#cdb38c;
  }
  *{margin:0;padding:0;box-sizing:border-box}
  html,body{width:1200px;height:783px;overflow:hidden;background:var(--white)}
  .spread{position:relative;width:1200px;height:783px;font-family:"Barlow",Arial,sans-serif;color:var(--ink)}

  .side-panel{position:absolute;top:0;width:211px;height:783px;background:var(--navy)}
  .side-panel--left{left:0}
  .side-panel--right{left:988px;width:212px}
  .accent-band{position:absolute;left:0;top:78px;width:100%;height:44px;background:var(--orange)}

  .brand{position:absolute;display:flex;align-items:center;gap:7px;color:var(--white)}
  .brand__dot{width:34px;height:34px;border-radius:50%;background:var(--orange);flex:none}
  .brand__name{font-weight:400;font-size:13px;line-height:14px}
  .brand--top{left:34px;top:23px}
  .brand--bottom{left:1004px;top:696px}

  .section-title{position:absolute;font-family:"Oswald",Arial,sans-serif;font-weight:600;color:var(--orange);font-size:28.5px;line-height:35px;letter-spacing:.2px}
  .section-title .num{position:absolute;left:-23px;top:0}
  .section-title--one{left:43px;top:128px}
  .section-title--two{left:31px;top:128px}
  .section-tag{position:absolute;font-style:italic;font-weight:600;color:var(--orange);font-size:11.5px}
  .section-tag--one{left:43px;top:306px}
  .section-tag--two{left:31px;top:205px}

  .photo{position:absolute}
  .photo--plant{left:36px;top:380px;width:164px;height:132px;background:linear-gradient(160deg,#8a929b,#d8dadc 55%,#f3f3f3)}
  .photo--box{left:600px;top:0;width:388px;height:248px;background:linear-gradient(140deg,#ffffff 0%,#eef0f1 45%,var(--photo-warm) 100%)}

  .copy{position:absolute;width:168px;font-family:"Barlow Semi Condensed","Barlow",Arial,sans-serif;font-weight:300;font-size:11.4px;line-height:15.45px;text-align:justify;hyphens:auto}
  .copy p+p{margin-top:4.5px}

  .uses-title{position:absolute;left:210px;top:534px;width:360px;text-align:center;font-weight:700;font-size:23.5px;color:var(--navy)}
  .uses-band{position:absolute;left:9px;top:571px;width:591px;height:153px;background:var(--orange)}
  .use{position:absolute;top:13px;width:108px;text-align:center}
  .use__photo{width:100px;height:100px;margin:0 auto;border-radius:50%;border:2.5px solid var(--navy)}
  .use__label{margin-top:8px;font-style:italic;font-size:10px;line-height:11.5px;color:var(--navy)}

  .pull-quote{position:absolute;left:645px;top:461px;width:324px;padding:4px 0 3px;border-top:1.3px solid var(--navy);border-bottom:1.3px solid var(--navy);font-style:italic;font-weight:600;font-size:13.2px;line-height:16.4px;color:var(--navy);text-align:justify;text-align-last:left}
</style>
</head>
<body>
<main class="spread">

  <aside class="side-panel side-panel--left">
    <div class="accent-band"></div>
    <div class="brand brand--top"><span class="brand__dot"></span><span class="brand__name">Unified EPS<br>Trade<br>Coalition</span></div>
    <h2 class="section-title section-title--one"><span class="num">1</span>ESSENTIAL<br>MARKETS<br>&amp; GLOBAL<br>DISTRIBUTION<br>NETWORKS</h2>
    <p class="section-tag section-tag--one">Abc?</p>
    <div class="photo photo--plant" role="img" aria-label="Worker handling white EPS containers in a production plant"></div>
  </aside>

  <div class="copy" style="left:220px;top:70px">
    <p>All protective packaging, whether plastic, fiber, pulp, or aluminum, exists to serve an essential purpose in global trade. The plastic pollution policy options under consideration will greatly impact packaging and product distribution channels and careful consideration of nuances and subtleties will allow these objectives to be achieved while avoiding unintended outcomes.</p>
    <p>Of particular importance, cold chain shipping ensures delicate and perishable agriculture and pharmaceutical products are safe, of high quality and never compromised. The EPS industry was instrumental in producing strictly specified, extreme low temperature-controlled shipping containers that allowed for the quick and safe distribution of COVID 19 vaccines around the world. EPS packaging is instrumental for wide-range of global medical applications, such as organ transport and pharmaceuticals.</p>
  </div>
  <div class="copy" style="left:397px;top:70px">
    <p>The ParcelWay Guides, which are based on test procedure requirements, recommend EPS packaging for essential products due to its ability to reduce the weight of containers and provide maximum inner protection during shipment. Nordhem has also deemed EPS essential for product protection, they found replacing EPS with paper-based materials increased environmental impacts for heavy and fragile products.</p>
    <p>Australia’s National Plastics Plan imposed a ban on single use plastics, that included EPS, however, they concluded EPS used for business-to-business and business-to-consumer packaging and specialized packaging used in medical and agricultural applications is out of the ban’s scope and has been deemed essential. EHAF, the home appliance association of Europe, stated a the implications of a proposed EPS ban in France “are significant to the home appliance industry.”</p>
  </div>

  <h2 class="uses-title">ESSENTIAL USES</h2>
  <section class="uses-band">
    <div class="use" style="left:22px"><div class="use__photo" role="img" aria-label="Washing machine packed in EPS" style="background:linear-gradient(150deg,#eef3f8,#9fb3c6)"></div><p class="use__label">Appliances</p></div>
    <div class="use" style="left:129px"><div class="use__photo" role="img" aria-label="Sample vials in an EPS tray" style="background:linear-gradient(150deg,#f4f1f7,#c6bedb)"></div><p class="use__label">Pharmaceutical</p></div>
    <div class="use" style="left:237px"><div class="use__photo" role="img" aria-label="Fresh fish on ice in an EPS box" style="background:linear-gradient(150deg,#dfe6ea,#8d9aa3)"></div><p class="use__label">Fresh Food<br>Distribution</p></div>
    <div class="use" style="left:344px"><div class="use__photo" role="img" aria-label="Printer held by EPS end caps" style="background:linear-gradient(150deg,#f5f5f5,#c9ccce)"></div><p class="use__label">Electronics</p></div>
    <div class="use" style="left:452px"><div class="use__photo" role="img" aria-label="Molded EPS automotive part" style="background:linear-gradient(150deg,#ffffff,#d4d6d8)"></div><p class="use__label">Automotive</p></div>
  </section>

  <div class="photo photo--box" role="img" aria-label="Hands fitting an EPS insert around a product inside a cardboard box"></div>

  <div class="copy" style="left:635px;top:266px">
    <p>Expanded polystyrene protective packaging use has largely been reduced to essential applications that require the unique performance properties of this material. Large appliances, electronics, pharmaceuticals, perishable, and delicate food products rely on EPS for global distribution.</p>
    <p>Through careful design and testing by knowledgeable packaging</p>
  </div>
  <div class="copy" style="left:811px;top:266px">
    <p>In addition to safety, health and legal factors when designing packaging, packaging engineers are concerned with efficient use of materials and production facilities as well as energy conservation and cost reduction.</p>
    <p>EPS manufacturers incorporate recycled content into their products by blending in used expanded particles from products they take in and grind down to the bead level. The average</p>
  </div>

  <p class="pull-quote">RECYCLED CONTENT EPS AS REDUCED VIRGIN RESIN CONSUMPTION BY AN AVERAGE OF 30 MILLION POUNDS OVER THE LAST DECADE</p>

  <div class="copy" style="left:635px;top:533px">
    <p>engineers, EPS packaging is specified to meet stringent delivery requirements, particularly in remote delivery areas, by using the least amount of material necessary. This is achieved by using void space, fluted wall design, and the latest packaging science technology such as CAD design to improve prototyping. This ensures the packaging is right sized and there is no material waste.</p>
  </div>
  <div class="copy" style="left:811px;top:533px">
    <p>recycled content rate is 30%. Additionally, EPS resin also incorporates recycled content by extruding and repelletizing 100 percent recovered EPS. EPS source reduction opportunities continue to evolve as the industry continues to establish innovative ways to boost recyclability and levels of recycled content while maintaining product performance.</p>
  </div>

  <aside class="side-panel side-panel--right">
    <div class="accent-band"></div>
    <h2 class="section-title section-title--two"><span class="num">2</span>SOURCE<br>REDUCTION</h2>
    <p class="section-tag section-tag--two">Conserving Resources</p>
  </aside>
  <div class="brand brand--bottom"><span class="brand__dot"></span><span class="brand__name">Unified EPS<br>Trade<br>Coalition</span></div>

</main>
</body>
</html>
```